Love pets? Create a veterinary business card that aligns with our new revamped website.

Greetings! We are a five-doctor veterinary hospital that seeks your expertise in designing a new business card that harmonizes with our recently revitalized website: www.lmcr.net. The card should feature our logo, the five doctors, operating hours, contact information, and communicate our purpose and personality.

Contact Information for Business Card

TBA

```html
<!DOCTYPE html>
<html lang="en">
<head>
<meta charset="utf-8">
<title>Lakemoor Creek Veterinary Hospital – Business Card</title>
<link rel="stylesheet" href="https://fonts.googleapis.com/css2?family=Cookie&family=Open+Sans:wght@400;600;700&display=swap">
<style>
  :root {
    --backdrop: #a8a8a8;
    --card-cream: #ece9e4;
    --card-green: #4a8a3e;
    --leaf-green: #3f8a3a;
    --brand-brown: #6b4a1a;
    --accent-orange: #d18a2c;
    --rule-grey: #9a9692;
    --back-text: #f1eee6;
  }
  * { box-sizing: border-box; margin: 0; padding: 0; }
  html, body { width: 1200px; height: 1000px; overflow: hidden; }
  body {
    background: var(--backdrop);
    position: relative;
    font-family: "Open Sans", Arial, sans-serif;
  }
  .card {
    position: absolute;
    left: 294px;
    width: 612px;
    height: 352px;
    border-radius: 24px;
    overflow: hidden;
  }
  .card-front { top: 85px; background: var(--card-cream); }
  .card-back { top: 523px; background: var(--card-green); }

  .brand-mark {
    position: absolute;
    left: 26px; top: 36px;
    display: flex; align-items: center; gap: 12px;
  }
  .brand-dot {
    width: 38px; height: 38px; border-radius: 50%;
    background: var(--leaf-green);
  }
  .brand-name {
    font-weight: 600; font-size: 22px; line-height: 1.15;
    color: var(--leaf-green);
  }

  .doctor-name {
    position: absolute; left: 31px; top: 176px;
    font-family: "Cookie", cursive;
    font-size: 44px; line-height: 1;
    color: var(--leaf-green);
  }
  .doctor-title {
    position: absolute; left: 31px; top: 219px;
    font-weight: 700; font-size: 17px;
    color: var(--brand-brown);
  }
  .divider {
    position: absolute; left: 26px; right: 26px; top: 256px;
    height: 2px; background: var(--rule-grey);
  }

  .contact-list {
    position: absolute; left: 34px; top: 268px;
    list-style: none;
    font-size: 16px; line-height: 23px;
    color: var(--leaf-green);
  }
  .contact-list li { display: flex; align-items: center; gap: 8px; }
  .contact-list svg { width: 14px; height: 14px; fill: var(--accent-orange); }

  .hours {
    position: absolute; left: 403px; top: 272px;
    display: flex; gap: 8px;
    font-size: 16px; line-height: 20px;
    color: var(--leaf-green);
  }
  .hours svg { width: 18px; height: 18px; margin-top: 2px; }
  .hours b { font-weight: 700; }

  .back-brand {
    position: absolute; right: 34px; top: 182px;
    text-align: right;
    font-weight: 600; font-size: 30px; line-height: 1.2;
    color: var(--back-text);
  }
  .back-web {
    position: absolute; left: 349px; top: 274px;
    display: flex; align-items: center; gap: 8px;
    font-size: 17px; color: var(--back-text);
  }
  .back-web svg { width: 17px; height: 17px; }
</style>
</head>
<body>
  <section class="card card-front">
    <div class="brand-mark">
      <span class="brand-dot"></span>
      <span class="brand-name">Lakemoor Creek<br>Veterinary Hospital</span>
    </div>

    <p class="doctor-name">Dan Mercer</p>
    <p class="doctor-title">DVM</p>
    <div class="divider"></div>

    <ul class="contact-list">
      <li>
        <svg viewBox="0 0 24 24"><path d="M6.6 10.8a15.1 15.1 0 0 0 6.6 6.6l2.2-2.2c.3-.3.7-.4 1-.2 1.1.4 2.3.6 3.6.6.6 0 1 .4 1 1V20c0 .6-.4 1-1 1A17 17 0 0 1 3 4c0-.6.4-1 1-1h3.5c.6 0 1 .4 1 1 0 1.3.2 2.5.6 3.6.1.3 0 .7-.2 1z"/></svg>
        (555) 210-4872
      </li>
      <li>
        <svg viewBox="0 0 24 24"><path d="M2 5h20v2l-10 6L2 7z"/><path d="M2 9l10 6 10-6v10H2z"/></svg>
        info@lmcr.net
      </li>
    </ul>

    <div class="hours">
      <svg viewBox="0 0 24 24"><circle cx="12" cy="12" r="11" fill="var(--accent-orange)"/><path d="M12 6v6l-3 4" stroke="#fff" stroke-width="2" fill="none" stroke-linecap="round"/></svg>
      <div>
        <div><b>Mon-Fri:</b> 7am-6pm</div>
        <div><b>Sat:</b> 8am-12pm</div>
      </div>
    </div>
  </section>

  <section class="card card-back">
    <p class="back-brand">Lakemoor Creek<br><span style="font-size:19px">Veterinary Hospital</span></p>
    <div class="back-web">
      <svg viewBox="0 0 24 24" fill="none" stroke="var(--back-text)" stroke-width="1.8"><circle cx="12" cy="12" r="10"/><path d="M2 12h20M12 2c3 3 3 17 0 20M12 2c-3 3-3 17 0 20"/></svg>
      www.lmcr.net
    </div>
  </section>
</body>
</html>
```